Creative Brief
Corporate Image - Harborline Estate Counsel
Business Card, Envelope, Post Card, Letterhead, Email Signature
Professional
Peter J. Linwood
Managing Attorney
418 Tamsin
Larkmoor KS 60000
(555) 555-HOME (4663)
pl@HarborlineEstateCounsel.example
www.HarborlineEstateCounsel.example
I am planning to go with a black glossy business card so the Logo looks more striking.
In my business, judgments about how good I am are often based on how fancy my "packaging" is. The documents produced are a very important part of that "packaging."
I envision the back of the card as one large logo and then somewhere on the back (in small print) the words:
Wills, Trusts, Asset Protection, Medicaid Planning, Special Needs Planning
Here is Logo file in Black
Logo - white background - words need to be more easily readable.

```html
<!DOCTYPE html>
<html lang="en">
<head>
<meta charset="utf-8">
<title>Harborline Estate Counsel – Business Card</title>
<link rel="stylesheet" href="https://fonts.googleapis.com/css2?family=Tinos:wght@400;700&display=swap">
<style>
  :root {
    --page: #e9e6e1;
    --card-black: #0b0b0c;
    --card-black-2: #1d1d1f;
    --silver-light: #f2f2f2;
    --name-light: #d4d4d6;
    --ink-dark: #161616;
    --ink-light: #e6e6e6;
  }
  html, body {
    margin: 0;
    width: 1200px;
    height: 976px;
    overflow: hidden;
    background: var(--page);
  }
  .canvas { position: relative; width: 1200px; height: 976px; }
  .card {
    position: absolute;
    width: 607px;
    height: 352px;
    border-radius: 16px;
    overflow: hidden;
    box-shadow: 0 10px 24px rgba(0,0,0,.28);
  }
  .card-front { left: 145px; top: 127px; background: var(--silver-light); }
  .card-back {
    left: 430px; top: 488px;
    background: radial-gradient(ellipse at 50% 35%, var(--card-black-2), var(--card-black) 70%);
  }
  .front-art { position: absolute; inset: 0; }
  .brand-name {
    position: absolute;
    left: 40px; top: 52px;
    font-family: "Tinos", serif;
    font-weight: 700;
    font-size: 30px;
    color: var(--name-light);
    margin: 0;
  }
  .person {
    position: absolute;
    left: 87px; top: 200px;
    font-family: "Tinos", serif;
    color: var(--ink-dark);
  }
  .person-name { font-weight: 700; font-size: 17px; margin: 0; }
  .person-title { font-size: 13px; margin: 2px 0 0; }
  .contact {
    position: absolute;
    right: 20px; top: 212px;
    text-align: right;
    font-family: "Tinos", serif;
    font-size: 13px;
    line-height: 17px;
    color: var(--ink-dark);
    margin: 0;
    font-style: normal;
  }
  .website {
    position: absolute;
    right: 20px; bottom: 20px;
    font-family: "Tinos", serif;
    font-weight: 700;
    font-size: 13px;
    color: var(--ink-dark);
    margin: 0;
  }
  .back-brand {
    position: absolute;
    left: 0; right: 0; top: 126px;
    text-align: center;
    font-family: "Tinos", serif;
    font-weight: 700;
    font-size: 34px;
    color: var(--name-light);
    margin: 0;
  }
  .services {
    position: absolute;
    left: 0; right: 0; top: 276px;
    text-align: center;
    font-family: "Tinos", serif;
    font-size: 15px;
    line-height: 20px;
    color: var(--ink-light);
    margin: 0;
  }
</style>
</head>
<body>
<main class="canvas">
  <section class="card card-front" aria-label="Business card front">
    <svg class="front-art" viewBox="0 0 607 352" preserveAspectRatio="none" aria-hidden="true">
      <defs>
        <linearGradient id="blackTop" x1="0" y1="0" x2="0" y2="1">
          <stop offset="0" stop-color="#1e1e20"/>
          <stop offset="1" stop-color="#050505"/>
        </linearGradient>
        <linearGradient id="silverBand" x1="0" y1="0" x2="1" y2="0">
          <stop offset="0" stop-color="#8a8a8d"/>
          <stop offset=".45" stop-color="#f4f4f4"/>
          <stop offset=".8" stop-color="#a9a9ac"/>
          <stop offset="1" stop-color="#e8e8e8"/>
        </linearGradient>
        <linearGradient id="silverBase" x1="0" y1="0" x2="1" y2="1">
          <stop offset="0" stop-color="#d3d3d5"/>
          <stop offset=".5" stop-color="#f7f7f7"/>
          <stop offset="1" stop-color="#c9c9cb"/>
        </linearGradient>
      </defs>
      <rect width="607" height="352" fill="url(#silverBase)"/>
      <path d="M0 0H607V112C510 150 420 118 323 150C225 182 108 150 0 214Z" fill="url(#silverBand)"/>
      <path d="M0 0H607V100C510 136 420 106 323 136C225 166 108 136 0 196Z" fill="url(#blackTop)"/>
      <path d="M0 214C108 150 225 182 323 150C420 118 510 150 607 112V124C510 162 420 132 323 162C225 194 108 166 0 224Z" fill="#2a2a2c"/>
    </svg>
    <h1 class="brand-name">Harborline Estate Counsel</h1>
    <div class="person">
      <p class="person-name">Peter J. Linwood</p>
      <p class="person-title">Managing Attorney</p>
    </div>
    <address class="contact">
      418 Tamsin, Larkmoor KS 60000<br>
      Phone: (555) 555-HOME (4663)<br>
      Fax: (555) 555-0142<br>
      Email: pl@HarborlineEstateCounsel.example
    </address>
    <p class="website">www.HarborlineEstateCounsel.example</p>
  </section>

  <section class="card card-back" aria-label="Business card back">
    <h2 class="back-brand">Harborline Estate Counsel</h2>
    <p class="services">
      Wills &nbsp;|&nbsp; Trusts &nbsp;|&nbsp; Asset Protection<br>
      Medicaid Planning &nbsp;|&nbsp; Special Needs Planning
    </p>
  </section>
</main>
</body>
</html>
```